Academy Values Classroom Poster

Marrowdene Community Academy has the core values of Aspiration, Positivity, Responsibility and Achievement at its heart. We have these words displayed in our entrance (in Bliss font) but would like them to permeate into the classroom spaces in a poster form. We want a clear message that shows what the values mean to students:

Aspiration - Think BIG (pantone 717)
Positivity - Smile :-) (pantone 376)
Responsibility - for yourself and others (pantone 569)
Achievement - Celebrate Success! (pantone 214)

It would be good to follow the colour scheme of the main words to create a 'brand' for these values (pantone refs noted in brackets) and we would like to see some clean designs please.

I anticipate these will be A1 posters.

I have attached our school logo although it is not essential that this is included.

Target Market(s)

Students

Industry/Entity Type

School

Font styles to use
Other font styles liked:
• Bliss or Segoe UI

Requirements
Must have
• Aspiration - Think BIG
Positivity - Smile :-)
Responsibility - for yourself and others
Achievement - Celebrate Success!
Should not have
• Nothing too busy

```html
<!DOCTYPE html>
<html lang="en">
<head>
<meta charset="utf-8">
<title>Academy Values Classroom Posters</title>
<link rel="stylesheet" href="https://fonts.googleapis.com/css2?family=Montserrat:ital,wght@0,600;0,800;1,800&family=Oswald:wght@700&display=swap">
<style>
  :root {
    --wall: #ececea;
    --ink: #111111;
    --paper: #ffffff;
    --positivity-green: #8cc63e;
    --achievement-pink: #e4157a;
    --achievement-yellow: #f6ee1c;
    --aspiration-orange: #f7931e;
    --aspiration-teal: #1a9a84;
    --responsibility-teal: #1a9a84;
    --responsibility-dark: #0f3b33;
    --responsibility-red: #f21e3c;
  }
  html, body {
    margin: 0;
    padding: 0;
    overflow: hidden;
    background: var(--wall);
  }
  .canvas {
    position: relative;
    width: 1200px;
    height: 838px;
    overflow: hidden;
    background: var(--wall);
  }
  .poster-row {
    position: absolute;
    left: 30px;
    top: 234px;
    display: flex;
    gap: 20px;
  }
  .poster {
    width: 270px;
    height: 370px;
    display: block;
  }
  .type-geo { font-family: "Montserrat", sans-serif; font-weight: 800; }
  .type-geo-medium { font-family: "Montserrat", sans-serif; font-weight: 600; }
  .type-condensed { font-family: "Oswald", sans-serif; font-weight: 700; }
</style>
</head>
<body>
<main class="canvas">
  <div class="poster-row">

    <!-- Positivity: Smile -->
    <svg class="poster poster-smile" viewBox="0 0 270 370" role="img" aria-label="Smile">
      <defs><clipPath id="smile-area"><rect x="10" y="10" width="250" height="350"/></clipPath></defs>
      <rect width="270" height="370" fill="var(--ink)"/>
      <rect x="10" y="10" width="250" height="350" fill="var(--positivity-green)"/>
      <g clip-path="url(#smile-area)">
        <text class="type-geo-medium" x="26" y="44" font-size="16" fill="var(--ink)" letter-spacing="9">SMILE</text>
        <text class="type-geo-medium" transform="translate(236 70) rotate(90)" font-size="15" fill="var(--ink)" letter-spacing="5">SMILE</text>
        <text class="type-geo-medium" transform="translate(176 112) rotate(180)" font-size="14" fill="var(--ink)" letter-spacing="3">SMILE</text>
        <text class="type-geo" transform="translate(72 292) rotate(-90)" font-size="50" fill="var(--paper)" textLength="180" lengthAdjust="spacingAndGlyphs">SMILE</text>
        <text class="type-geo" transform="translate(96 254) rotate(-40)" font-size="38" fill="var(--paper)" stroke="var(--ink)" stroke-width="3" paint-order="stroke" textLength="150" lengthAdjust="spacingAndGlyphs">SMILE</text>
        <text class="type-geo" transform="rotate(-12 135 318)" x="28" y="340" font-size="62" fill="var(--paper)" textLength="214" lengthAdjust="spacingAndGlyphs">SMILE</text>
      </g>
    </svg>

    <!-- Achievement: Celebrate Success -->
    <svg class="poster poster-celebrate" viewBox="0 0 270 370" role="img" aria-label="Celebrate Success!">
      <defs><clipPath id="celebrate-area"><rect x="10" y="10" width="250" height="350"/></clipPath></defs>
      <rect width="270" height="370" fill="var(--paper)"/>
      <rect x="10" y="10" width="250" height="350" fill="var(--achievement-pink)"/>
      <g clip-path="url(#celebrate-area)">
        <g stroke="var(--achievement-yellow)" stroke-width="3">
          <line x1="30" y1="128" x2="34" y2="156"/>
          <line x1="228" y1="58" x2="238" y2="90"/>
          <line x1="236" y1="138" x2="244" y2="168"/>
        </g>
        <text class="type-geo" x="30" y="110" font-size="60" fill="var(--paper)" stroke="var(--ink)" stroke-width="3" paint-order="stroke" textLength="190" lengthAdjust="spacingAndGlyphs" rotate="-4 3 -3 5">CELE</text>
        <text class="type-geo" x="30" y="212" font-size="54" fill="var(--paper)" stroke="var(--ink)" stroke-width="3" paint-order="stroke" textLength="200" lengthAdjust="spacingAndGlyphs" rotate="0 -5 4 -6 3">BRATE</text>
        <g transform="translate(24 330) skewX(-10)">
          <text class="type-condensed" x="0" y="0" font-size="76" fill="var(--achievement-yellow)" stroke="var(--ink)" stroke-width="3" paint-order="stroke" textLength="212" lengthAdjust="spacingAndGlyphs">SUCCESS!</text>
        </g>
      </g>
    </svg>

    <!-- Aspiration: Think Big -->
    <svg class="poster poster-think-big" viewBox="0 0 270 370" role="img" aria-label="Think Big">
      <defs><clipPath id="big-area"><rect x="10" y="10" width="250" height="350"/></clipPath></defs>
      <rect width="270" height="370" fill="var(--ink)"/>
      <rect x="10" y="10" width="250" height="350" fill="var(--aspiration-orange)"/>
      <g clip-path="url(#big-area)">
        <text class="type-geo" x="32" y="66" font-size="42" font-style="italic" fill="var(--paper)" stroke="var(--ink)" stroke-width="1.5" textLength="204" lengthAdjust="spacingAndGlyphs">THINK</text>
        <g class="type-condensed" font-size="240" fill="none" stroke="var(--ink)" stroke-width="2">
          <text x="40" y="336" textLength="204" lengthAdjust="spacingAndGlyphs">BIG</text>
          <text x="46" y="342" textLength="204" lengthAdjust="spacingAndGlyphs">BIG</text>
        </g>
        <text class="type-condensed" x="32" y="330" font-size="240" fill="var(--aspiration-teal)" stroke="var(--ink)" stroke-width="2" textLength="204" lengthAdjust="spacingAndGlyphs">BIG</text>
      </g>
    </svg>

    <!-- Responsibility: For yourself and others -->
    <svg class="poster poster-responsibility" viewBox="0 0 270 370" role="img" aria-label="Responsibility for yourself and others">
      <defs>
        <clipPath id="responsibility-area"><rect x="10" y="10" width="250" height="350"/></clipPath>
        <path id="responsibility-arc" d="M 22 92 Q 135 200 248 82"/>
      </defs>
      <rect width="270" height="370" fill="var(--paper)"/>
      <rect x="10" y="10" width="250" height="350" fill="var(--responsibility-teal)"/>
      <g clip-path="url(#responsibility-area)">
        <text class="type-geo-medium" x="135" y="76" text-anchor="middle" font-size="30" fill="var(--paper)" stroke="var(--ink)" stroke-width="0.8" letter-spacing="10">FOR</text>
        <text class="type-geo-medium" font-size="21" fill="var(--paper)" stroke="var(--ink)" stroke-width="0.7" text-anchor="middle">
          <textPath href="#responsibility-arc" startOffset="50%">RESPONSIBILITY</textPath>
        </text>
        <text class="type-geo" x="135" y="206" text-anchor="middle" font-size="34" fill="var(--responsibility-dark)" stroke="var(--ink)" stroke-width="1" textLength="224" lengthAdjust="spacingAndGlyphs">YOURSELF</text>
        <g class="type-geo" font-size="36" font-style="italic" fill="var(--responsibility-red)" stroke="var(--ink)" stroke-width="1">
          <text x="135" y="262" text-anchor="middle" letter-spacing="4">AND</text>
          <text x="40" y="332">O</text>
          <text x="72" y="332">T</text>
          <text x="104" y="302">H</text>
          <text x="136" y="322">E</text>
          <text x="166" y="332">R</text>
          <text x="196" y="332">S</text>
        </g>
      </g>
    </svg>

  </div>
</main>
</body>
</html>
```